Tarvimo Software (a new software house) needs a Wordpress web site

We need a Wordpress web site. We develop innovative software as a service (on demand) for companies and cunsumers.
Updates

Project Deadline Extended
Reason: I need extra days to analyze.

Target Market(s)

Consumers who use mobile software to access useful information about your day by day in a crowd plataform and on demand.

Industry/Entity Type

Software

Requirements
Must have
• See wordpress template suggestion:
http://themes.plondavi.com/?theme=marbleton

```html
<!DOCTYPE html>
<html lang="en">
<head>
<meta charset="utf-8">
<title>Tarvimo Software</title>
<link href="https://fonts.googleapis.com/css2?family=Orbitron:wght@500;700;900&family=Carlito:ital,wght@0,400;0,700;1,400&display=swap" rel="stylesheet">
<style>
  :root {
    --green: #1ed64a;
    --green-light: #b9f3c5;
    --nav-grey: #6b6b6b;
    --nav-muted: #b08cb0;
    --logo-dark: #111111;
    --blue: #5a8fd0;
    --blue-dark: #2a5fb0;
    --text: #222222;
    --text-soft: #555555;
    --heading-grey: #8a8a8a;
    --orange: #ff6a00;
    --panel: #dedede;
    --footer-light: #a6a6a6;
    --footer-dark: #6a6a6a;
    --title-steel: #9aa6c6;
    --title-shadow: #7a5a7a;
    --field-top: #4a4a4a;
    --field-bottom: #050505;
  }
  * { box-sizing: border-box; margin: 0; padding: 0; }
  html, body { width: 1000px; height: 1200px; overflow: hidden; }
  body { font-family: "Carlito", "Calibri", sans-serif; color: var(--text); background: #ffffff; }
  .page { position: relative; width: 1000px; height: 1200px; overflow: hidden; }
  .abs { position: absolute; }

  /* Hero */
  .hero {
    position: absolute; left: 0; top: 0; width: 1000px; height: 365px;
    background:
      radial-gradient(ellipse 300px 160px at 150px 200px, rgba(255,255,255,.7), transparent 70%),
      radial-gradient(ellipse 320px 170px at 720px 180px, rgba(255,255,255,.75), transparent 70%),
      radial-gradient(ellipse 260px 120px at 480px 60px, rgba(255,255,255,.45), transparent 70%),
      radial-gradient(ellipse 300px 140px at 880px 320px, rgba(255,255,255,.5), transparent 70%),
      var(--green);
  }
  .brand { position: absolute; left: 12px; top: 22px; display: flex; align-items: center; gap: 14px; }
  .brand-mark { width: 44px; height: 44px; border-radius: 50%; background: var(--logo-dark); }
  .brand-name { font-family: "Carlito", sans-serif; font-weight: 700; font-size: 30px; line-height: 1; color: var(--logo-dark); }
  .main-nav a {
    position: absolute; top: 29px; font-family: "Orbitron", sans-serif; font-weight: 700;
    font-size: 15px; letter-spacing: .5px; color: var(--nav-grey); text-decoration: none;
  }
  .main-nav a.muted { color: var(--nav-muted); }
  .hero-art { position: absolute; left: 78px; top: 150px; width: 244px; height: 168px; border-radius: 14px;
    background: linear-gradient(135deg, #6f9fe6, #1f4fa8); }
  .hero-title { position: absolute; font-family: "Orbitron", sans-serif; font-weight: 900; color: var(--title-steel);
    text-shadow: 3px 3px 0 var(--title-shadow), 6px 6px 8px rgba(0,0,0,.25); font-style: normal; line-height: 1; }
  .hero-title.one { left: 462px; top: 120px; font-size: 66px; letter-spacing: 2px; }
  .hero-title.two { left: 438px; top: 196px; font-size: 80px; letter-spacing: 1px; }
  .hero-copy { position: absolute; left: 355px; top: 289px; width: 612px; font-size: 11px; line-height: 13.6px; color: #111; }

  /* Services */
  .services { position: absolute; left: 0; top: 370px; width: 1000px; height: 205px;
    background: linear-gradient(#ffffff, #ececec); }
  .service { position: absolute; top: 0; width: 190px; }
  .service-label { position: absolute; top: 14px; font-size: 23px; font-weight: 700; color: var(--heading-grey); white-space: nowrap; }
  .service-icon { position: absolute; left: 0; top: 47px; width: 56px; height: 62px; border-radius: 50%; }
  .service-title { position: absolute; top: 52px; font-family: "Orbitron", sans-serif; font-weight: 900; font-size: 19px; color: var(--blue); white-space: nowrap; }
  .service-sub { position: absolute; top: 79px; font-size: 17px; color: var(--text); white-space: nowrap; }
  .service-sub.small { font-size: 14px; top: 82px; }
  .service-text { position: absolute; left: 0; top: 125px; width: 180px; font-size: 14px; line-height: 17px; color: var(--text); }

  /* Tagline band */
  .tagline { position: absolute; left: 0; top: 575px; width: 1000px; height: 57px;
    background: linear-gradient(#ececec, #ffffff 40%, #d4d4d4);
    text-align: center; font-family: "Orbitron", sans-serif; font-weight: 700; font-size: 34px;
    line-height: 36px; padding-top: 1px; color: #333; letter-spacing: 1px; }
  .tagline em { font-style: normal; color: var(--orange); }
  .tagline-shadow { position: absolute; left: 0; top: 632px; width: 1000px; height: 8px;
    background: linear-gradient(#555, #dedede); }

  /* Products */
  .products { position: absolute; left: 0; top: 640px; width: 1000px; height: 328px;
    background: linear-gradient(#e4e4e4, #d3d3d3); }
  .products-heading { position: absolute; left: 105px; top: 5px; font-size: 32px; font-style: italic; color: #333; font-weight: 400; }
  .product { position: absolute; width: 300px; height: 80px; }
  .product-img { position: absolute; left: 0; top: 0; width: 62px; height: 58px; border-radius: 50%; }
  .product-name { position: absolute; top: 0; font-size: 24px; color: #333; white-space: nowrap; }
  .product-desc { position: absolute; top: 32px; font-size: 14px; line-height: 20px; color: var(--text-soft); letter-spacing: .3px; }
  .product-feature { position: absolute; left: 780px; top: 62px; width: 110px; height: 110px; border-radius: 8px;
    background: linear-gradient(#f5a623 0 22%, #ecece4 22%, #b5b5a8); }
  .blog-link { position: absolute; left: 744px; top: 270px; display: flex; align-items: center; gap: 12px; font-size: 16px; color: #333; }
  .blog-badges { display: flex; gap: 2px; }
  .blog-badges span { width: 23px; height: 23px; border-radius: 50%; background: #444; border: 2px solid #bbb;
    color: #eee; font-family: "Orbitron", sans-serif; font-size: 10px; font-weight: 700; display: flex; align-items: center; justify-content: center; }

  /* Footer */
  .footer { position: absolute; left: 0; top: 968px; width: 1000px; height: 232px;
    background: radial-gradient(ellipse 420px 260px at 430px 80px, var(--footer-light), var(--footer-dark)); }
  .footer-heading { position: absolute; top: 12px; font-size: 22px; font-weight: 700; text-shadow: 1px 1px 2px rgba(255,255,255,.6); }
  .footer-heading.follow { left: 312px; color: var(--orange); }
  .footer-heading.contact { left: 707px; color: var(--blue); font-weight: 400; }
  .social { position: absolute; display: flex; align-items: center; gap: 8px; font-size: 12px; color: #f2f2f2; }
  .social.stacked { flex-direction: column; gap: 3px; }
  .social-square { width: 58px; height: 58px; border-radius: 6px; background: #3c3c3c; }
  .field { position: absolute; left: 707px; width: 165px; border-radius: 7px; border: 1px solid #9a9a9a;
    background: linear-gradient(var(--field-top), var(--field-bottom) 60%); color: #eee; font-size: 11px; padding: 3px 10px; }
  .field.name { top: 70px; height: 26px; }
  .field.email { top: 117px; height: 26px; }
  .field.message { top: 162px; height: 62px; }
</style>
</head>
<body>
<div class="page">

  <header class="hero">
    <div class="brand">
      <span class="brand-mark"></span>
      <span class="brand-name">Tarvimo Software</span>
    </div>
    <nav class="main-nav">
      <a href="#" style="left:355px">PRODUCTS</a>
      <a href="#" style="left:495px">SERVICES</a>
      <a href="#" style="left:647px">PORTOFOLIO</a>
      <a href="#" class="muted" style="left:828px">COMPANY</a>
    </nav>
    <div class="hero-art" role="img" aria-label="Illustration of a blue book with a question mark on the cover"></div>
    <h1 class="hero-title one">CUSTOM</h1>
    <div class="hero-title two">SOFTWARE</div>
    <p class="hero-copy">Lorem ipsum dolor sit amet, consectetur adipiscing elit. Suspendisse venenatis, neque ac tempus tincidunt, mi ante tempus metus, ac ultricies dui odio eu est. Vestibulum non dignissim quam. Fusce viverra convallis sapien, at eleifend neque tincidunt malesuada. Curabitur ullamcorper quam ac adipiscing molestie. Vestibulum pretium eros nisl, ac consequat velit sodales tempus. Donec ut egestas metus. Proin leo quam, interdum sit amet ipsum eget, imperdiet congue magna. Etiam pharetra quam id congue facilisis. Quisque dignissim facilisis diam, sit amet dictum sapien scelerisque non. Maecenas id vehicula odio.</p>
  </header>

  <section class="services">
    <div class="service" style="left:104px">
      <div class="service-label" style="left:27px">ANALYSE</div>
      <div class="service-icon" style="background:radial-gradient(#e6e6e6,#9a9a9a)" role="img" aria-label="Icon of a silver key"></div>
      <div class="service-title" style="left:62px">ANALYSIS</div>
      <div class="service-sub" style="left:62px">of your needs</div>
      <p class="service-text">Contrary to popular belief, Lorem Ipsum is not simply random text. It has roots in a</p>
    </div>
    <div class="service" style="left:296px">
      <div class="service-label" style="left:18px">DEVELOPMENT</div>
      <div class="service-icon" style="left:0;background:radial-gradient(#f2f2f2,#8c8c8c)" role="img" aria-label="Icon of a metal gear"></div>
      <div class="service-title" style="left:68px">DEVELOP</div>
      <div class="service-sub" style="left:62px">&amp; create application</div>
      <p class="service-text" style="left:7px">Contrary to popular belief, Lorem Ipsum is not simply random text. It has roots in a</p>
    </div>
    <div class="service" style="left:502px">
      <div class="service-label" style="left:15px">CUSTOMIZE</div>
      <div class="service-icon" style="left:10px;background:radial-gradient(#444,#000)" role="img" aria-label="Icon of a black top hat with red band"></div>
      <div class="service-title" style="left:83px">FITTING</div>
      <div class="service-sub" style="left:71px">to activities</div>
      <p class="service-text">Contrary to popular belief, Lorem Ipsum is not simply random text. It has roots in a</p>
    </div>
    <div class="service" style="left:700px">
      <div class="service-label" style="left:14px">ASSISTANCE</div>
      <div class="service-icon" style="width:60px;height:60px;background:radial-gradient(#ffffff 55%,#222 60%)" role="img" aria-label="Icon of a wall clock"></div>
      <div class="service-title" style="left:70px">LONG TERM</div>
      <div class="service-sub small" style="left:70px">partnership</div>
      <p class="service-text" style="left:3px">Contrary to popular belief, Lorem Ipsum is not simply random text. It has roots in a</p>
    </div>
  </section>

  <h2 class="tagline">TIME TO HAVE <em>YOUR SOFTWARE</em></h2>
  <div class="tagline-shadow"></div>

  <section class="products">
    <h2 class="products-heading">Our products</h2>
    <div class="product" style="left:107px;top:70px">
      <div class="product-img" style="background:radial-gradient(#c8ef5a,#7cbf1e)" role="img" aria-label="Icon of a green cake"></div>
      <div class="product-name" style="left:78px">Lorem ipsum dolor</div>
      <p class="product-desc" style="left:79px">Pellentesque habitant morbi<br>tristique senectus et netus</p>
    </div>
    <div class="product" style="left:415px;top:72px">
      <div class="product-img" style="top:-4px;height:48px;background:radial-gradient(#ffb347,#e8730c)" role="img" aria-label="Icon of a fruit pie"></div>
      <div class="product-name" style="left:85px">Lorem ipsum dolor</div>
      <p class="product-desc" style="left:87px">Pellentesque habitant morbi<br>tristique senectus et netus</p>
    </div>
    <div class="product-feature" role="img" aria-label="Illustration of an open box with glowing eyes inside"></div>
    <div class="product" style="left:107px;top:225px">
      <div class="product-img" style="top:2px;height:48px;background:radial-gradient(#c79a5a,#4a2612)" role="img" aria-label="Icon of assorted chocolates"></div>
      <div class="product-name" style="left:78px">Lorem ipsum dolor</div>
      <p class="product-desc" style="left:79px">Pellentesque habitant morbi<br>tristique senectus et netus</p>
    </div>
    <div class="product" style="left:415px;top:225px">
      <div class="product-img" style="top:2px;height:48px;background:radial-gradient(#7a4320,#4a230c 60%,#e8b070 62%)" role="img" aria-label="Icon of a chocolate donut"></div>
      <div class="product-name" style="left:85px">Lorem ipsum dolor</div>
      <p class="product-desc" style="left:87px">Pellentesque habitant morbi<br>tristique senectus et netus</p>
    </div>
    <a class="blog-link">check our
      <span class="blog-badges"><span>B</span><span>L</span><span>O</span><span>G</span></span>
    </a>
  </section>

  <footer class="footer">
    <h3 class="footer-heading follow">FOLLOW US</h3>
    <div class="social stacked" style="left:310px;top:71px"><span class="social-square"></span>Friendlo</div>
    <div class="social stacked" style="left:413px;top:71px"><span class="social-square"></span>Chirpway</div>
    <div class="social" style="left:310px;top:164px"><span class="social-square"></span>Circlemark</div>

    <h3 class="footer-heading contact">Contact Us</h3>
    <div class="field name">name</div>
    <div class="field email">email</div>
    <div class="field message">message</div>
  </footer>

</div>
</body>
</html>
```